Sunny Paths and joy Business card

I have a logo, but will like a business card design. Is for a travel agency in Mexico. We focus in family experiences.

I will liek some thing different and unique, from the traditional business card, something to get remmeber for.

Business card information:

Leandro T. Ocampo
leandro@sunnypathsjoy.example

Alameda 482, 3 piso
Col. Tlalpizco
Mexico, D.F. 07320

office: (55) 5000-0142
mobile: (55) 9000-0187

www.sunnypathsjoy.example
@sunnypjoy
blog: sunnypathsandjoy.blogsite.example
facebook: SunnyPathsAndJoy

```html
<!DOCTYPE html>
<html lang="en">
<head>
<meta charset="utf-8">
<title>Sunny Paths and joy – Business card</title>
<link rel="stylesheet" href="https://fonts.googleapis.com/css2?family=Arimo:wght@400;700&display=swap">
<style>
  :root {
    --page: #e9e7e2;
    --card: #ffffff;
    --sky: #b3d6f0;
    --sky-pale: #dbeaf7;
    --cloud: #d6e8f6;
    --brand: #1d4f9e;
    --ink-light: #ffffff;
    --shadow: rgba(40, 40, 40, 0.18);
  }
  * { box-sizing: border-box; margin: 0; padding: 0; }
  html, body {
    width: 1200px; height: 900px; overflow: hidden;
    background: var(--page);
    font-family: "Arimo", Arial, sans-serif;
  }
  .canvas {
    position: relative; width: 1200px; height: 900px;
  }
  .card {
    position: absolute; left: 250px; width: 700px; height: 400px;
    background: var(--card); overflow: hidden;
    box-shadow: 0 6px 18px var(--shadow);
  }
  .card--front { top: 40px; }
  .card--back { top: 470px; }

  /* front */
  .cloud {
    position: absolute; background: var(--cloud); border-radius: 60px;
  }
  .cloud--top-left { left: 30px; top: 70px; width: 190px; height: 70px; }
  .cloud--bottom-right { right: 25px; top: 240px; width: 150px; height: 80px; }
  .front-brand {
    position: absolute; left: 0; right: 0; top: 150px;
    display: flex; flex-direction: column; align-items: center; gap: 22px;
  }
  .brand-mark {
    display: flex; align-items: center; gap: 14px;
    color: var(--brand); font-weight: 700;
  }
  .brand-mark__dot {
    border-radius: 50%; background: var(--brand);
  }
  .front-brand .brand-mark { font-size: 44px; }
  .front-brand .brand-mark__dot { width: 34px; height: 34px; }
  .front-brand__web {
    color: var(--brand); font-size: 20px; letter-spacing: 0.5px;
  }

  /* back */
  .back-brand {
    position: absolute; left: 36px; top: 40px;
  }
  .back-brand .brand-mark { font-size: 22px; gap: 9px; }
  .back-brand .brand-mark__dot { width: 18px; height: 18px; }
  .sky-band { position: absolute; left: 0; top: 0; width: 700px; height: 400px; }
  .contact {
    position: absolute; right: 30px; top: 108px;
    text-align: right; color: var(--ink-light);
    font-size: 14px; line-height: 18px;
  }
  .contact__name { font-size: 22px; font-weight: 700; line-height: 28px; letter-spacing: 0.5px; }
  .contact__group { margin-top: 12px; }
  .contact__group--tight { margin-top: 2px; }
</style>
</head>
<body>
<main class="canvas">

  <section class="card card--front" aria-label="Card front">
    <div class="cloud cloud--top-left" role="img" aria-label="Soft light blue clouds"></div>
    <div class="cloud cloud--bottom-right" role="img" aria-label="Soft light blue clouds"></div>
    <div class="front-brand">
      <div class="brand-mark"><span class="brand-mark__dot"></span><span>Sunny Paths and joy</span></div>
      <p class="front-brand__web">www.sunnypathsjoy.example</p>
    </div>
  </section>

  <section class="card card--back" aria-label="Card back">
    <div class="back-brand">
      <div class="brand-mark"><span class="brand-mark__dot"></span><span>Sunny Paths and joy</span></div>
    </div>
    <svg class="sky-band" viewBox="0 0 700 400" aria-hidden="true">
      <g transform="translate(0,-14)">
        <path fill="var(--sky-pale)" d="M0 200 C40 170 90 170 130 185 C170 120 260 110 320 135 C380 80 560 70 640 110 C665 98 690 96 700 100 L700 414 L0 414 Z"/>
      </g>
      <g transform="translate(0,-5)">
        <path fill="#ffffff" d="M0 200 C40 170 90 170 130 185 C170 120 260 110 320 135 C380 80 560 70 640 110 C665 98 690 96 700 100 L700 405 L0 405 Z"/>
      </g>
      <path fill="var(--sky)" d="M0 200 C40 170 90 170 130 185 C170 120 260 110 320 135 C380 80 560 70 640 110 C665 98 690 96 700 100 L700 400 L0 400 Z"/>
    </svg>
    <div class="contact">
      <p class="contact__name">Leandro T. Ocampo</p>
      <p>leandro@sunnypathsjoy.example</p>
      <div class="contact__group">
        <p>Alameda 482, 3 piso</p>
        <p>Col. Tlalpizco</p>
        <p>Mexico, D.F. 07320</p>
      </div>
      <div class="contact__group">
        <p>office: (55) 5000-0142</p>
        <p>mobile: (55) 9000-0187</p>
      </div>
      <div class="contact__group">
        <p>@sunnypjoy</p>
        <p>blog: sunnypathsandjoy.blogsite.example</p>
        <p>facebook: SunnyPathsAndJoy</p>
      </div>
    </div>
  </section>

</main>
</body>
</html>
```